Kestrel Fitness Studio Retail Tube Design

We require a design for cardboard tubes, like images included, which will be the main packaging for the clothing sold in our fitness studio. Kestrel Fitness Studio is an upscale customer service driven fitness studio that is geared towards improving our clients/members quality of life by marrying cutting edge technology like 3D scanning and metabolic measurement with first class training based on 30+ years of experience in the industry.

The project will require a design which revolves around the tube seamlessly including the lid and its top and must include the company logo, which is included, along with our web address (www.kestrelgymhall.example).

The final design should be a bold, sleek design which stands out so when people see the tube they will either know it’s from our studio or be curious as to want company it’s from. Similar to the impact the Moravanti bag has that is given to all their customers.

Target Market(s)

Individuals and groups seeking individualize fitness programs which produce results.

Industry/Entity Type

Clothing

Colors

Designer to choose colors to be used in the design.

Requirements
Must have
• Logo and website address

```html
<!DOCTYPE html>
<html lang="en">
<head>
<meta charset="utf-8">
<title>Kestrel Fitness Studio – Retail Tube Wrap</title>
<link href="https://fonts.googleapis.com/css2?family=Ubuntu:ital,wght@0,300;0,400;0,700;1,700&display=swap" rel="stylesheet">
<style>
  :root {
    --bg: #dedede;
    --paper: #f4f4f2;
    --red: #d81f26;
    --red-deep: #a30d12;
    --black: #151515;
    --white: #ffffff;
    --ink: #2a2a2a;
  }
  html, body {
    margin: 0;
    width: 1167px;
    height: 1200px;
    overflow: hidden;
    background: var(--bg);
    font-family: "Ubuntu", sans-serif;
  }
  .canvas { position: relative; width: 1167px; height: 1200px; }
  .tube {
    position: absolute;
    left: 462px; top: 112px;
    width: 252px; height: 1000px;
    overflow: hidden;
    background: var(--paper);
  }
  .lid {
    position: absolute; left: 0; top: 0;
    width: 252px; height: 232px;
    background: var(--paper);
    text-align: center;
  }
  .brand-mark {
    position: absolute; left: 112px; top: 62px;
    width: 28px; height: 28px;
    background: var(--red);
  }
  .brand-name {
    position: absolute; left: 0; right: 0; top: 150px;
    color: var(--ink);
    font-weight: 300;
    font-size: 44px;
    line-height: 1;
    letter-spacing: 1px;
  }
  .brand-sub {
    position: absolute; left: 0; right: 0; top: 204px;
    color: var(--ink);
    font-weight: 300;
    font-size: 13px;
    letter-spacing: 2.5px;
  }
  .block { position: absolute; }
  .red { background: var(--red); }
  .red-deep { background: var(--red-deep); }
  .black { background: var(--black); }
  .slogan {
    position: absolute;
    writing-mode: vertical-rl;
    white-space: nowrap;
    font-weight: 700;
    line-height: 1;
  }
  .slogan.white { color: var(--white); }
  .slogan.accent { color: var(--red); }
  .slogan.italic { font-style: italic; }
  .web {
    position: absolute;
    writing-mode: vertical-rl;
    white-space: nowrap;
    color: var(--white);
    font-weight: 400;
    font-size: 16px;
  }
</style>
</head>
<body>
<div class="canvas">
  <div class="tube">
    <div class="lid">
      <div class="brand-mark"></div>
      <div class="brand-name">kestrel</div>
      <div class="brand-sub">FITNESS STUDIO</div>
    </div>

    <!-- column: born to lift -->
    <div class="block red" style="left:0;top:232px;width:28px;height:88px;"></div>
    <div class="block black" style="left:0;top:320px;width:28px;height:680px;"></div>
    <div class="slogan white italic" style="left:2px;top:352px;font-size:24px;">I was born to LIFT</div>

    <!-- column: web address -->
    <div class="block black" style="left:30px;top:232px;width:54px;height:518px;"></div>
    <div class="block red" style="left:30px;top:756px;width:54px;height:244px;"></div>
    <div class="web" style="left:45px;top:380px;">www.kestrelgymhall.example</div>

    <!-- column: sweat smile repeat -->
    <div class="block red" style="left:88px;top:232px;width:64px;height:488px;"></div>
    <div class="block black" style="left:88px;top:726px;width:64px;height:274px;"></div>
    <div class="slogan white" style="left:99px;top:296px;font-size:40px;">Sweat, Smile</div>
    <div class="slogan white" style="left:99px;top:742px;font-size:38px;">and REPEAT</div>

    <!-- column: pinstripes -->
    <div class="block black" style="left:157px;top:232px;width:5px;height:768px;"></div>
    <div class="block black" style="left:166px;top:232px;width:4px;height:768px;"></div>
    <div class="block black" style="left:174px;top:232px;width:6px;height:768px;"></div>

    <!-- column: go workout -->
    <div class="block red" style="left:184px;top:232px;width:34px;height:40px;"></div>
    <div class="block black" style="left:184px;top:720px;width:34px;height:280px;"></div>
    <div class="slogan accent" style="left:184px;top:296px;font-size:36px;">GO WORKOUT</div>

    <!-- column: log off -->
    <div class="block black" style="left:220px;top:232px;width:32px;height:276px;"></div>
    <div class="block red-deep" style="left:220px;top:514px;width:32px;height:486px;"></div>
    <div class="slogan white" style="left:222px;top:298px;font-size:32px;">log off.</div>
  </div>
</div>
</body>
</html>
```